Business card design for sports medicine and athlete care clinic.

We need a bold, solid business card design for our practitioners to stand out. We treat overuse & sports-related injuries and provide post-operative rehabilitation. Our specialisations include chronic conditions, men’s health, nutrition & musculoskeletal disorders (MSDs). All brand collateral in terms of fonts, logo and colour palette to be provided.

Target Market(s)

Athletes (professional and amateur), sportspeople, predominantly male

Industry/Entity Type

Health And Wellness

Contact Information for Business Card

The front of the card should be white with dark blue text the back dark blue with white text. The logo should be top-left. The business name should be horizontal and right of the logo. The tagline should be directly below centred on the back of the card (see top-banner.png and bottom-banner.png)

Font styles to use
Sans Serif

Colors
0355a3
0293ce
3176b5
ffffff
85acd3

Requirements
Nice to have
• Diagonal and/or horizontal line elements between logo and practitioner details and/or bottom corner of card (see slide.png and tag-bg.png).

```html
<!DOCTYPE html>
<html lang="en">
<head>
<meta charset="utf-8">
<title>Stride Point Clinic – Business Card</title>
<link rel="stylesheet" href="https://fonts.googleapis.com/css2?family=Montserrat:ital,wght@0,500;0,700;0,800;1,600&family=Questrial&display=swap">
<style>
  :root {
    --navy: #0b2a6f;
    --deep-blue: #0355a3;
    --sky-blue: #0293ce;
    --mid-blue: #3176b5;
    --soft-blue: #85acd3;
    --white: #ffffff;
    --stage: #3a3a3c;
    --ink: #1b1f3a;
  }
  * { box-sizing: border-box; margin: 0; padding: 0; }
  html, body { width: 1200px; height: 866px; overflow: hidden; }
  body {
    background: var(--stage);
    display: flex;
    flex-direction: column;
    align-items: center;
    justify-content: center;
    gap: 22px;
    font-family: "Questrial", "Century Gothic", sans-serif;
  }
  .card {
    position: relative;
    width: 700px;
    height: 400px;
    overflow: hidden;
    box-shadow: 0 10px 24px rgba(0,0,0,0.45);
  }

  /* Front */
  .card--front { background: var(--white); color: var(--ink); }
  .front__decor {
    position: absolute;
    left: 0; top: 0;
    width: 330px; height: 260px;
    background: radial-gradient(ellipse at 35% 35%, rgba(133,172,211,0.28), rgba(133,172,211,0.08) 55%, rgba(255,255,255,0) 75%);
  }
  .brand {
    position: absolute;
    left: 300px; top: 56px;
    display: flex; align-items: center; gap: 12px;
  }
  .brand__dot {
    width: 30px; height: 30px; border-radius: 50%;
    background: var(--sky-blue);
  }
  .brand__name {
    font-family: "Montserrat", sans-serif;
    font-weight: 800;
    font-size: 27px;
    color: var(--navy);
    letter-spacing: 0.3px;
  }
  .brand__tagline {
    position: absolute;
    left: 342px; top: 96px;
    font-family: "Montserrat", sans-serif;
    font-style: italic;
    font-weight: 600;
    font-size: 14.5px;
    color: var(--sky-blue);
  }
  .person { position: absolute; left: 56px; top: 150px; }
  .person__name {
    font-family: "Montserrat", sans-serif;
    font-weight: 800;
    font-size: 27px;
    color: var(--navy);
  }
  .person__role { font-size: 16px; color: #2b2f45; margin-top: 2px; }
  .contact { list-style: none; margin-top: 14px; }
  .contact li {
    display: flex; align-items: center; gap: 9px;
    font-size: 15px; line-height: 24px; color: #23263a;
  }
  .contact svg { width: 17px; height: 17px; flex: none; }
  .social {
    position: absolute; right: 56px; bottom: 108px;
    display: flex; align-items: center; gap: 8px;
    font-size: 16px; color: var(--navy);
  }
  .social__dot { width: 14px; height: 14px; border-radius: 50%; background: var(--mid-blue); }
  .address {
    position: absolute; right: 56px; bottom: 44px;
    font-size: 16px; line-height: 22px; color: #23263a; text-align: right;
  }
  .front__line {
    position: absolute; left: 56px; right: 56px; top: 132px;
    height: 2px;
    background: linear-gradient(90deg, var(--sky-blue), rgba(133,172,211,0));
  }

  /* Back */
  .card--back {
    background: linear-gradient(35deg, var(--sky-blue) 0%, var(--deep-blue) 45%, var(--navy) 100%);
    color: var(--white);
  }
  .back__decor {
    position: absolute; inset: 0;
    background: radial-gradient(ellipse at 30% 30%, rgba(255,255,255,0.10), rgba(255,255,255,0) 55%),
                radial-gradient(ellipse at 75% 80%, rgba(133,172,211,0.10), rgba(255,255,255,0) 50%);
  }
  .back__content {
    position: absolute; inset: 0;
    display: flex; flex-direction: column; align-items: center; justify-content: center;
  }
  .back__brand { display: flex; align-items: center; gap: 14px; }
  .back__dot { width: 34px; height: 34px; border-radius: 50%; background: var(--white); }
  .back__name {
    font-family: "Montserrat", sans-serif;
    font-weight: 800; font-size: 34px; color: var(--white);
  }
  .back__tagline {
    font-family: "Montserrat", sans-serif;
    font-style: italic; font-weight: 600;
    font-size: 17px; margin-top: 8px; margin-left: 48px;
  }
  .services {
    display: flex; align-items: center; gap: 12px;
    font-size: 17px; margin-top: 44px;
  }
  .services__sep { width: 7px; height: 7px; border-radius: 50%; background: var(--white); }
</style>
</head>
<body>

  <section class="card card--front" aria-label="Business card front">
    <div class="front__decor" role="img" aria-label="Faint illustration of athletes in motion"></div>

    <div class="brand">
      <span class="brand__dot"></span>
      <span class="brand__name">Stride Point Clinic</span>
    </div>
    <p class="brand__tagline">Sports medicine and athlete care</p>

    <div class="front__line"></div>

    <div class="person">
      <h1 class="person__name">Daniel Hart</h1>
      <p class="person__role">Managing Director</p>
      <ul class="contact">
        <li>
          <svg viewBox="0 0 20 20" aria-hidden="true"><circle cx="10" cy="10" r="10" fill="#0b2a6f"/><path d="M7 5.5l1.6 0 .8 2.4-1.1.8a6 6 0 0 0 3 3l.8-1.1 2.4.8v1.6c0 .6-.5 1-1.1 1A8 8 0 0 1 6 6.6c0-.6.4-1.1 1-1.1z" fill="#fff"/></svg>
          044-987 654 321
        </li>
        <li>
          <svg viewBox="0 0 20 20" aria-hidden="true"><circle cx="10" cy="10" r="10" fill="#0b2a6f"/><rect x="5" y="6.5" width="10" height="7" fill="none" stroke="#fff" stroke-width="1.3"/><path d="M5 6.5l5 4 5-4" fill="none" stroke="#fff" stroke-width="1.3"/></svg>
          hello@stridepoint.com
        </li>
        <li>
          <svg viewBox="0 0 20 20" aria-hidden="true"><circle cx="10" cy="10" r="10" fill="#0b2a6f"/><circle cx="10" cy="10" r="5.5" fill="none" stroke="#fff" stroke-width="1.2"/><ellipse cx="10" cy="10" rx="2.3" ry="5.5" fill="none" stroke="#fff" stroke-width="1.1"/><path d="M4.5 10h11" stroke="#fff" stroke-width="1.1"/></svg>
          www.stridepointclinic.com.au
        </li>
      </ul>
    </div>

    <div class="social">
      <span class="social__dot"></span>
      <span>StridePointAU</span>
    </div>
    <p class="address">17, Harbour Street Northside<br>30218, Country Name</p>
  </section>

  <section class="card card--back" aria-label="Business card back">
    <div class="back__decor" role="img" aria-label="Faint illustration of athletes in motion"></div>
    <div class="back__content">
      <div class="back__brand">
        <span class="back__dot"></span>
        <span class="back__name">Stride Point Clinic</span>
      </div>
      <p class="back__tagline">Sports medicine and athlete care</p>
      <div class="services">
        <span>Coaching</span><span class="services__sep"></span>
        <span>Dietetics</span><span class="services__sep"></span>
        <span>Massage Therapy</span>
      </div>
    </div>
  </section>

</body>
</html>
```